Exciting Personal Development Book Cover: FIND ZEN NOW!

Design a Book Cover for my personal development book.
Title: Find Zen Now!
Author: Marcus Telly
Tagline: A practical path to calm focus and steady momentum

My picture must make up the front cover as I need to build my brand and people should recognise me on book shelves. Bold and catchy. How you do it is up to you. There must be space for a short testimonial from a famous person who is currently reading my book. I uploaded a sample of what I made in Photoshop but I don't have design skills.

I've added a PDF of my book so you can read the chapter index and introduction to get a sense of the content.

Target Market(s)

Personal Development Self-Help Market

Industry/Entity Type

Personal Development

Font styles to use
Serif
Sans Serif

Requirements
Must have
• My picture as hero image on cover.
Nice to have
• Must have Title, Tagline and my author name. If possible ZEN stands for 'Zeal, Energy & Nerve' If there is a way to fit this somewhere great. If it's too much then it can go somewhere on the back.

```html
<!DOCTYPE html>
<html lang="en">
<head>
<meta charset="utf-8">
<title>Find Zen Now! – Book Cover Spread</title>
<link rel="stylesheet" href="https://fonts.googleapis.com/css2?family=Oswald:wght@600;700&family=Roboto:ital,wght@0,400;0,700;0,900;1,700;1,900&display=swap">
<style>
  :root {
    --page-bg: #ffffff;
    --charcoal: #3a3d41;
    --charcoal-dark: #2e3134;
    --slate-light: #8a8e92;
    --slate-mid: #5c6065;
    --yellow: #d8cb3c;
    --navy: #1f2c3d;
    --white: #ffffff;
    --skin-tone: #c49a84;
    --shirt-tone: #eceef0;
  }
  * { box-sizing: border-box; margin: 0; padding: 0; }
  html, body {
    width: 1200px; height: 1200px; overflow: hidden;
    background: var(--page-bg);
  }
  .canvas { position: relative; width: 1200px; height: 1200px; }

  .spread {
    position: absolute; left: 26px; top: 216px;
    width: 1148px; height: 770px;
    overflow: hidden;
  }

  /* Back cover */
  .back-cover {
    position: absolute; left: 0; top: 0; width: 538px; height: 770px;
    background: radial-gradient(ellipse at 50% 40%, #45484c 0%, var(--charcoal) 55%, var(--charcoal-dark) 100%);
  }
  .back-blurb {
    position: absolute; left: 70px; top: 90px; width: 410px;
    font-family: "Roboto", sans-serif; font-size: 12.6px; line-height: 1.42;
    color: var(--white); text-align: justify;
  }
  .back-blurb p + p { margin-top: 16px; }

  /* Shared yellow band */
  .title-band {
    position: absolute; left: 0; top: 510px; width: 1148px; height: 133px;
    background: var(--yellow);
  }
  .back-testimonial {
    position: absolute; left: 0; top: 536px; width: 538px; text-align: center;
  }
  .back-testimonial .quote {
    font-family: "Roboto", sans-serif; font-style: italic; font-weight: 900;
    font-size: 19px; line-height: 1.15; color: var(--white); text-transform: uppercase;
  }
  .back-testimonial .source {
    margin-top: 6px;
    font-family: "Roboto", sans-serif; font-weight: 700; font-size: 18px;
    color: var(--navy); text-transform: uppercase;
  }

  /* Spine: reads bottom to top – author, title, tagline */
  .spine {
    position: absolute; left: 538px; top: 0; width: 68px; height: 770px;
    background: var(--yellow);
  }
  .spine-inner {
    position: absolute; left: 0; top: 770px;
    width: 770px; height: 68px;
    transform-origin: 0 0; transform: rotate(-90deg);
    display: flex; align-items: center;
    padding: 0 14px 0 52px;
  }
  .spine-author {
    font-family: "Roboto", sans-serif; font-weight: 900; font-size: 22px;
    color: var(--white); letter-spacing: 1px; white-space: nowrap;
  }
  .spine-title {
    margin-left: 36px;
    font-family: "Oswald", sans-serif; font-weight: 700; font-size: 44px;
    color: var(--navy); letter-spacing: 1px; white-space: nowrap; line-height: 1;
  }
  .spine-tagline {
    margin-left: 14px;
    font-family: "Oswald", sans-serif; font-weight: 600; font-size: 13px; line-height: 1.25;
    color: var(--navy); text-transform: uppercase; letter-spacing: 0.4px;
    white-space: nowrap;
  }

  /* Front cover */
  .front-cover {
    position: absolute; left: 606px; top: 0; width: 542px; height: 770px;
    background: radial-gradient(ellipse at 60% 30%, var(--slate-light) 0%, var(--slate-mid) 50%, #45484c 100%);
    overflow: hidden;
  }
  .front-author {
    position: absolute; left: 0; top: 40px; width: 542px; text-align: center;
    padding-left: 30px;
    font-family: "Roboto", sans-serif; font-weight: 900; font-size: 46px;
    color: var(--yellow); letter-spacing: 2px;
  }
  .author-portrait {
    position: absolute; left: 66px; top: 114px; width: 476px; height: 656px;
    background:
      radial-gradient(ellipse 70px 90px at 52% 22%, var(--skin-tone) 0%, var(--skin-tone) 70%, transparent 72%),
      radial-gradient(ellipse 230px 330px at 50% 78%, var(--shirt-tone) 0%, var(--shirt-tone) 70%, transparent 72%);
    opacity: 0.9;
  }
  .front-testimonial {
    position: absolute; left: 30px; top: 262px; width: 160px;
  }
  .front-testimonial .quote {
    font-family: "Roboto", sans-serif; font-style: italic; font-weight: 900;
    font-size: 16px; line-height: 1.12; color: var(--white); text-transform: uppercase;
  }
  .front-testimonial .source {
    margin-top: 4px;
    font-family: "Roboto", sans-serif; font-weight: 700; font-size: 16px;
    color: var(--navy); text-transform: uppercase;
  }
  .front-band {
    position: absolute; left: 0; top: 510px; width: 542px; height: 133px;
    background: var(--yellow); opacity: 0.93;
    text-align: center; padding-top: 14px;
  }
  .front-title {
    font-family: "Oswald", sans-serif; font-weight: 700; font-size: 80px;
    line-height: 1; color: var(--navy); letter-spacing: 1px;
  }
  .front-tagline {
    margin-top: 8px;
    font-family: "Oswald", sans-serif; font-weight: 600; font-size: 13.5px;
    color: var(--navy); text-transform: uppercase; letter-spacing: 0.6px;
  }
</style>
</head>
<body>
<main class="canvas">
  <section class="spread">

    <div class="back-cover">
      <div class="back-blurb">
        <p>Lorem ipsum dolor sit amet. Illum atque qui itaque saepe et vero porro eum aliquid sint qui dolores dolores ut dolor magnam. Qui aperiam accusamus in sunt et velit magni qui eveniet tempora et consectetur reprehenderit ea expedita molestiae! Aut nihil eaque et dolorum dolorem ut vero dolorum aut repudiandae sunt.</p>
        <p>Ut corporis maiores et repellendus possimus ut ipsam voluptas aut molestiae quisquam ex unde labore. Qui quae obcaecati ea molestiae esse et sint suscipit est voluptate vero!</p>
        <p>Aut iste dolor sit accusamus voluptates qui nobis quasi sit quae molestias quo veniam voluptas. Sit doloribus provident in eaque consequuntur et commodi impedit ad nemo rerum quo earum voluptatem? Et maiores voluptate est nostrum vero sit nesciunt Quis ut facere saepe et harum quia. Est mollitia natus eum qui-squam architecto sit veritatis delectus est minima internos est dolor quis aut fugiat explicabo nam dolorem doloremque. voluptatem? Et maiores voluptate est nostrum vero sit nesciunt Quis ut facere saepe et harum quia. Est mollitia natus eum qui-squam architecto sit veritatis delectus est minima internos est dolor quis aut fugiat explicabo nam dolorem doloremque.</p>
      </div>
    </div>

    <div class="title-band"></div>

    <div class="back-testimonial">
      <p class="quote">“Lorem ipsum dolor sit amet,<br>consectetur adipiscing elit”</p>
      <p class="source">Name Surname</p>
    </div>

    <div class="spine">
      <div class="spine-inner">
        <span class="spine-author">MARCUS TELLY</span>
        <span class="spine-title">FIND ZEN NOW!</span>
        <span class="spine-tagline">A practical path to calm<br>focus and steady momentum</span>
      </div>
    </div>

    <div class="front-cover">
      <h2 class="front-author">MARCUS TELLY</h2>
      <div class="author-portrait" role="img" aria-label="Portrait photograph of the author, smiling, in a white open-collar shirt with tattooed forearms crossed"></div>
      <div class="front-testimonial">
        <p class="quote">“Lorem ipsum dolor sit amet, consectetur adipiscing elit”</p>
        <p class="source">Name Surname</p>
      </div>
      <div class="front-band">
        <h1 class="front-title">FIND ZEN NOW!</h1>
        <p class="front-tagline">A practical path to calm focus and steady momentum</p>
      </div>
    </div>

  </section>
</main>
</body>
</html>
```